Marlo's Pizzeria BOGO Promotion Pizza Flyer (Huron)

Pizzeria flyer promoting "under new management" and then the main point for this flyer is our Buy One Get One Free promotion on our pizzas (disclaimer: not valid for Mini Feast Tray or Crowd Pies)(we reserve the right to cancel this promotion at any time)
This promotion has no limit and can be carryout or delivery. No coupon needed.
Looking for a fun bright flyer with our logo colors

Requirements
Must have
• Store Info
• 287 Wexford Rd. E
• Huron, OH
• 419-867-2093
• Open at 4pm Daily!

```html
<!DOCTYPE html>
<html lang="en">
<head>
<meta charset="utf-8">
<title>Marlo's Pizzeria – Buy 1 Get 1 Free Flyer</title>
<link rel="stylesheet" href="https://fonts.googleapis.com/css2?family=Alfa+Slab+One&family=Passion+One:wght@700&family=Kaushan+Script&family=Oswald:wght@500;700&family=Archivo+Black&family=Roboto:wght@400;700&display=swap">
<style>
  :root{
    --page:#e7e4e0;
    --brick-dark:#3a140c;
    --brick:#7a2a16;
    --brick-light:#9c3b1e;
    --red:#c4161c;
    --deep-red:#8a0f12;
    --yellow:#ffd21f;
    --gold:#f5a300;
    --orange:#f07a12;
    --white:#ffffff;
    --chalk:#22392f;
    --chalk-light:#2f4d40;
    --frame:#8a5a2b;
    --parchment:#dcc596;
    --icon:#1a1a1a;
  }
  *{box-sizing:border-box;margin:0;padding:0}
  html,body{width:1200px;height:800px;overflow:hidden;background:var(--page)}
  .flyer{
    position:absolute;left:330px;top:20px;width:540px;height:760px;overflow:hidden;
    background:linear-gradient(180deg,var(--brick-dark) 0%,var(--brick) 35%,var(--brick-light) 55%,var(--brick) 70%);
    box-shadow:0 6px 18px rgba(0,0,0,.25);
  }
  .photo{position:absolute}
  .photo--pizza-corner{left:0;top:40px;width:130px;height:150px;
    background:radial-gradient(circle at 40% 50%,#e0a040 0%,#b8421c 55%,rgba(122,42,22,0) 75%)}
  .photo--vegetables{right:0;top:0;width:150px;height:200px;
    background:radial-gradient(circle at 60% 35%,#e83a1e 0%,#f0b020 35%,#3f8a2a 55%,rgba(122,42,22,0) 78%)}
  .photo--fire-pizza{left:0;top:470px;width:540px;height:290px;
    background:linear-gradient(180deg,rgba(240,110,20,0) 0%,#e25a12 22%,#c8321a 45%,#d98a3a 70%,#b8481c 100%)}
  .logo{
    position:absolute;left:160px;top:38px;width:148px;height:148px;border-radius:50%;
    background:var(--white);display:flex;align-items:center;justify-content:center;text-align:center;
    box-shadow:0 3px 8px rgba(0,0,0,.4);
  }
  .logo__name{font-family:'Oswald',sans-serif;font-weight:700;font-size:22px;line-height:1.1;color:var(--red);text-transform:uppercase}
  .tag-management{
    position:absolute;left:22px;top:196px;width:140px;height:62px;background:var(--parchment);
    transform:rotate(-14deg);display:flex;align-items:center;justify-content:center;text-align:center;
    font-family:'Alfa Slab One',serif;font-size:14px;line-height:1.1;color:var(--deep-red);
    box-shadow:0 3px 6px rgba(0,0,0,.4);
  }
  .headline__buy{position:absolute;left:46px;top:284px;font-family:'Alfa Slab One',serif;font-size:50px;line-height:1;color:var(--white);
    text-shadow:0 3px 0 #5a1a10,0 4px 8px rgba(0,0,0,.5)}
  .headline__free{position:absolute;left:186px;top:196px;font-family:'Passion One',sans-serif;font-weight:700;font-size:112px;line-height:1;color:var(--red);
    -webkit-text-stroke:4px var(--yellow);paint-order:stroke fill;transform:rotate(-8deg);transform-origin:left bottom;white-space:nowrap;
    text-shadow:0 4px 8px rgba(0,0,0,.5)}
  .headline__get{position:absolute;left:80px;top:322px;font-family:'Kaushan Script',cursive;font-size:74px;line-height:1;color:var(--yellow);
    text-shadow:0 3px 6px rgba(0,0,0,.55)}
  .headline__promo{position:absolute;left:206px;top:322px;font-family:'Oswald',sans-serif;font-weight:700;font-size:26px;line-height:1.2;color:var(--white);white-space:nowrap;
    transform:rotate(-8deg);transform-origin:left center;text-shadow:0 2px 4px rgba(0,0,0,.6)}
  .chalkboard{
    position:absolute;left:170px;top:392px;width:330px;height:150px;
    background:radial-gradient(ellipse at 50% 40%,var(--chalk-light),var(--chalk));
    border:7px solid var(--frame);box-shadow:0 6px 12px rgba(0,0,0,.55);
    display:flex;flex-direction:column;align-items:center;justify-content:center;text-align:center;padding:10px 14px;gap:6px;
  }
  .chalkboard__disclaimer{font-family:'Oswald',sans-serif;font-weight:500;font-size:10.5px;color:var(--white);letter-spacing:.3px}
  .chalkboard__terms{font-family:'Oswald',sans-serif;font-weight:700;font-size:17px;line-height:1.1;color:var(--yellow);text-transform:uppercase}
  .chalkboard__coupon{font-family:'Oswald',sans-serif;font-weight:700;font-size:32px;line-height:1;color:var(--red);
    -webkit-text-stroke:3px var(--white);paint-order:stroke fill;text-transform:uppercase}
  .badge-hours{
    position:absolute;left:28px;top:530px;width:104px;height:104px;border-radius:50%;
    background:radial-gradient(circle at 40% 35%,#ffe45a,var(--gold));border:3px solid var(--deep-red);
    display:flex;flex-direction:column;align-items:center;justify-content:center;transform:rotate(-12deg);
    font-family:'Alfa Slab One',serif;color:var(--deep-red);line-height:1;text-align:center;z-index:2;
  }
  .badge-hours__small{font-size:13px}
  .badge-hours__big{font-size:28px}
  .ribbon{position:absolute;left:0;top:612px;width:540px;height:110px}
  .ribbon svg{position:absolute}
  .ribbon__band{left:0;top:0}
  .ribbon__icon{left:58px;top:39px}
  .ribbon__number{position:absolute;left:100px;top:38px;font-family:'Archivo Black',sans-serif;font-size:32px;line-height:1;color:var(--deep-red);white-space:nowrap}
  .ribbon__divider{position:absolute;left:380px;top:26px;width:2px;height:58px;background:var(--deep-red)}
  .store-info{position:absolute;left:390px;top:28px;font-family:'Roboto',sans-serif;font-style:normal;font-size:13px;line-height:1.3;color:var(--deep-red);white-space:nowrap}
  .store-info__title{font-weight:700;text-transform:uppercase}
</style>
</head>
<body>
  <main class="flyer">
    <div class="photo photo--pizza-corner" role="img" aria-label="Pizza with fork and knife"></div>
    <div class="photo photo--vegetables" role="img" aria-label="Fresh tomatoes, peppers and herbs"></div>
    <div class="photo photo--fire-pizza" role="img" aria-label="Pizzas over flames"></div>

    <div class="logo"><span class="logo__name">Marlo's<br>Pizzeria</span></div>

    <div class="tag-management">UNDER NEW<br>MANAGEMENT</div>

    <h1 class="headline">
      <span class="headline__buy">BUY</span>
      <span class="headline__free">1FREE</span>
      <span class="headline__get">Get</span>
      <span class="headline__promo">PROMOTION ON OUR PIZZAS</span>
    </h1>

    <section class="chalkboard">
      <p class="chalkboard__disclaimer">WE RESERVE THE RIGHT TO CANCEL THIS PROMOTION AT ANY TIME</p>
      <p class="chalkboard__terms">This promotion has no limit and<br>can be carryout or delivery.</p>
      <p class="chalkboard__coupon">No coupon needed.</p>
    </section>

    <div class="badge-hours">
      <span class="badge-hours__small">OPEN AT</span>
      <span class="badge-hours__big">4PM</span>
      <span class="badge-hours__small">DAILY!</span>
    </div>

    <section class="ribbon">
      <svg class="ribbon__band" width="540" height="110" viewBox="0 0 540 110" aria-hidden="true">
        <defs>
          <linearGradient id="ribbonFill" x1="0" y1="0" x2="0" y2="1">
            <stop offset="0" stop-color="#ffd21f"/>
            <stop offset="1" stop-color="#f07a12"/>
          </linearGradient>
        </defs>
        <polygon points="18,18 540,6 540,96 18,100 40,60" fill="url(#ribbonFill)"/>
        <polygon points="18,18 540,6 540,12 22,24" fill="#fff3a0" opacity=".6"/>
      </svg>
      <svg class="ribbon__icon" width="32" height="32" viewBox="0 0 24 24" aria-hidden="true">
        <rect x="1" y="1" width="22" height="22" rx="4" fill="#1a1a1a"/>
        <path d="M8.2 5.5l2 2.4-1.2 1.6c.9 1.9 2.4 3.4 4.3 4.3l1.6-1.2 2.4 2-1.4 2.2c-4.9-.4-9.5-5-9.9-9.9z" fill="#ffd21f"/>
      </svg>
      <span class="ribbon__number">419-867-2093</span>
      <span class="ribbon__divider"></span>
      <address class="store-info">
        <span class="store-info__title">Store Info</span><br>
        287 Wexford Rd. E<br>
        Huron, OH
      </address>
    </section>
  </main>
</body>
</html>
```